Product Development PLAV (The Brambleford Leisure Works)

We are a sporting goods company who engages in "Total product Development" from A - Z incorporating customer collaboration and input. We research, collaborate and design, build, and ship for the customer. We have a PPT page which describes this process, but it is BORING and lacks "Fun". Our industry is an OUTDOOR company - Camping, Hunting, Fishing, etc. This process needs to be an illustration of the process and emphasizing the company process with fun illustrations.

Industry/Entity Type

It Company

```html
<!DOCTYPE html>
<html lang="en">
<head>
<meta charset="utf-8">
<title>Total Product Development Process</title>
<link href="https://fonts.googleapis.com/css2?family=Oswald:wght@700&display=swap" rel="stylesheet">
<style>
  :root {
    --bg: #f4f4f4;
    --bg-stripe: #ececec;
    --white: #ffffff;
    --green-1: #a6d234;
    --green-2: #96c924;
    --green-3: #86bb00;
    --blue-1: #0170c0;
    --blue-2: #0997ef;
    --blue-3: #4db2f7;
    --red-1: #ff5341;
    --red-2: #fe3a22;
    --red-3: #d91b00;
  }
  html, body { margin: 0; padding: 0; overflow: hidden; }
  .process-canvas {
    position: relative;
    width: 1200px;
    height: 1023px;
    overflow: hidden;
    background: repeating-linear-gradient(135deg, var(--bg) 0 6px, var(--bg-stripe) 6px 8px);
    font-family: "Oswald", "Arial Narrow", sans-serif;
  }
  .process-graphic { position: absolute; inset: 0; }
  .step-label {
    position: absolute;
    width: 300px;
    margin-left: -150px;
    text-align: center;
    color: var(--white);
    font-weight: 700;
    font-size: 31px;
    line-height: 41px;
    letter-spacing: 0.3px;
    text-transform: uppercase;
  }
  .icon-line { fill: none; stroke: var(--white); stroke-width: 4; stroke-linecap: round; stroke-linejoin: round; }
  .icon-fill { fill: var(--white); }
</style>
</head>
<body>
<main class="process-canvas">
  <svg class="process-graphic" width="1200" height="1023" viewBox="0 0 1200 1023" aria-hidden="true">
    <!-- Row 1: research -->
    <g class="row-research">
      <polygon fill="var(--green-1)" points="108,155 425,155 466,259 425,363 108,363 150,259"/>
      <polygon fill="var(--green-2)" points="425,155 743,155 784,259 743,363 425,363 466,259"/>
      <polygon fill="var(--green-3)" points="743,155 1062,155 1103,259 1062,363 743,363 784,259"/>
    </g>
    <!-- Row 2: build -->
    <g class="row-build">
      <polygon fill="var(--blue-1)" points="140,442 458,442 417,546 458,650 140,650 98,546"/>
      <polygon fill="var(--blue-2)" points="458,442 776,442 735,546 776,650 458,650 417,546"/>
      <polygon fill="var(--blue-3)" points="776,442 1092,442 1052,546 1092,650 776,650 735,546"/>
    </g>
    <!-- Row 3: ship -->
    <g class="row-ship">
      <polygon fill="var(--red-1)" points="108,728 425,728 466,832 425,936 108,936 150,832"/>
      <polygon fill="var(--red-2)" points="425,728 743,728 784,832 743,936 425,936 466,832"/>
      <polygon fill="var(--red-3)" points="743,728 1062,728 1103,832 1062,936 743,936 784,832"/>
    </g>

    <!-- Badges -->
    <g class="badge badge-collaboration" transform="translate(287,152)">
      <circle r="63" fill="var(--white)"/><circle r="51" fill="var(--green-1)"/>
      <path class="icon-line" d="M-30,-4 L-16,-16 L-2,-10 L10,-16 L30,-4 M-26,0 L-8,16 Q-2,22 4,16 L20,2 M-4,-8 L10,6 M-12,8 L-4,16 M-6,2 L4,12"/>
    </g>
    <g class="badge badge-design" transform="translate(605,152)">
      <circle r="63" fill="var(--white)"/><circle r="51" fill="var(--green-2)"/>
      <circle cx="-6" cy="-8" r="13" class="icon-line" stroke-width="9" stroke-dasharray="5 4"/>
      <circle cx="-6" cy="-8" r="7" class="icon-line"/>
      <circle cx="-22" cy="16" r="8" class="icon-line" stroke-width="6" stroke-dasharray="3.5 3"/>
      <circle cx="16" cy="18" r="6" class="icon-line" stroke-width="5" stroke-dasharray="3 2.5"/>
    </g>
    <g class="badge badge-sourcing" transform="translate(922,152)">
      <circle r="63" fill="var(--white)"/><circle r="51" fill="var(--green-3)"/>
      <circle cy="-4" r="24" class="icon-line"/>
      <path class="icon-line" d="M-24,-4 H24 M0,-28 V20 M-10,-26 Q-20,-4 -10,18 M10,-26 Q20,-4 10,18 M0,20 V30 M-12,32 H12"/>
    </g>
    <g class="badge badge-testing" transform="translate(277,440)">
      <circle r="63" fill="var(--white)"/><circle r="51" fill="var(--blue-1)"/>
      <rect x="-22" y="-28" width="38" height="50" rx="4" class="icon-line"/>
      <path class="icon-line" d="M-14,-16 H8 M-14,-6 H8 M-14,4 H0"/>
      <path class="icon-line" stroke-width="6" d="M4,14 L12,22 L28,4"/>
    </g>
    <g class="badge badge-quality" transform="translate(595,440)">
      <circle r="63" fill="var(--white)"/><circle r="51" fill="var(--blue-2)"/>
      <rect x="-26" y="-6" width="12" height="30" rx="2" class="icon-fill"/>
      <path class="icon-fill" d="M-10,-6 L0,-20 L2,-32 Q10,-32 10,-22 L8,-8 H24 Q30,-8 28,0 L22,20 Q20,24 14,24 H-10 Z"/>
    </g>
    <g class="badge badge-manufacturing" transform="translate(915,440)">
      <circle r="63" fill="var(--white)"/><circle r="51" fill="var(--blue-3)"/>
      <rect x="-26" y="-18" width="52" height="38" rx="3" class="icon-line" stroke-width="3" stroke-dasharray="6 5"/>
      <path class="icon-fill" d="M4,-14 Q4,-26 16,-26 Q26,-26 27,-16 Q34,-15 34,-9 Q34,-4 28,-4 H6 Q0,-4 0,-9 Q0,-14 4,-14 Z"/>
      <path class="icon-fill" d="M-28,18 Q-28,8 -18,8 Q-10,8 -8,15 Q-2,15 -2,21 Q-2,26 -8,26 H-26 Q-32,26 -32,21 Q-32,18 -28,18 Z"/>
    </g>
    <g class="badge badge-service" transform="translate(287,726)">
      <circle r="63" fill="var(--white)"/><circle r="51" fill="var(--red-1)"/>
      <path class="icon-line" stroke-width="5" d="M-24,2 V-6 Q-24,-30 0,-30 Q24,-30 24,-6 V2"/>
      <rect x="-30" y="-6" width="11" height="20" rx="4" class="icon-fill"/>
      <rect x="19" y="-6" width="11" height="20" rx="4" class="icon-fill"/>
      <path class="icon-line" d="M24,14 Q22,28 4,28"/>
      <circle cx="2" cy="28" r="4" class="icon-fill"/>
    </g>
    <g class="badge badge-fulfillment" transform="translate(605,726)">
      <circle r="63" fill="var(--white)"/><circle r="51" fill="var(--red-2)"/>
      <path class="icon-fill" d="M-26,-10 L4,-22 L30,-12 L30,18 L2,28 L-26,18 Z"/>
      <path d="M2,-4 V26 M-26,-10 L2,-2 L30,-12" fill="none" stroke="var(--red-2)" stroke-width="3"/>
      <path d="M16,14 V2 M12,6 L16,2 L20,6 M24,12 V0" fill="none" stroke="var(--red-2)" stroke-width="2.5"/>
      <circle cx="-18" cy="18" r="11" fill="var(--red-2)" stroke="var(--white)" stroke-width="3"/>
      <path class="icon-line" stroke-width="3" d="M-23,18 L-19,22 L-12,14"/>
    </g>
    <g class="badge badge-warehousing" transform="translate(922,726)">
      <circle r="63" fill="var(--white)"/><circle r="51" fill="var(--red-3)"/>
      <path class="icon-fill" d="M-32,16 V0 H-20 L-14,-14 H-2 V16 Z"/>
      <rect x="2" y="-26" width="4" height="44" class="icon-fill"/>
      <rect x="6" y="14" width="22" height="4" class="icon-fill"/>
      <rect x="9" y="-14" width="20" height="26" class="icon-line" stroke-width="3"/>
      <path class="icon-line" stroke-width="2.5" d="M9,-14 L29,12 M29,-14 L9,12"/>
      <circle cx="-24" cy="20" r="6" class="icon-fill" stroke="var(--red-3)" stroke-width="2"/>
      <circle cx="-6" cy="20" r="6" class="icon-fill" stroke="var(--red-3)" stroke-width="2"/>
    </g>
  </svg>

  <div class="step-label" style="left:287px; top:247px;">Customer<br>Collaboration</div>
  <div class="step-label" style="left:605px; top:247px;">Design &amp;<br>Develoment</div>
  <div class="step-label" style="left:922px; top:247px;">Global<br>Sourcing</div>

  <div class="step-label" style="left:277px; top:532px;">Product<br>Testing</div>
  <div class="step-label" style="left:595px; top:532px;">Quality<br>Assurance</div>
  <div class="step-label" style="left:912px; top:555px;">Manufacturing</div>

  <div class="step-label" style="left:287px; top:817px;">Customer<br>Service</div>
  <div class="step-label" style="left:605px; top:817px;">Fulfillment &amp;<br>Distribution</div>
  <div class="step-label" style="left:922px; top:817px;">Warehousing -<br>JIT Inventory</div>
</main>
</body>
</html>
```